Parkinson's Disease Progression

Visually describe the rate of Parkinson progression in the first 15 years following diagnosis. Title: "Patient-Perceived Progression of Parkinsonism"

The attached figure names "meanqol" is the curve that should serve as the basis of this graphic. Everything else-- color, labels, font, etc. describe this curve.
Thank you!

Target Market(s)

People with Parkisnon's Disease, neurologists, family members.

Font styles to use
Sans Serif

Requirements
Must have
• Must have the lines going through these exact numbers
Excellent -- 502
Very good- 661
Good- 895
Fair- 1268
Poor- 1655

LABELS:
Title: "Patient-Perceived Progression of Parkinsonism"
"SAW-MX (Self-Assessed Wellbeing Index for Movement Conditions)" should be the label on the left.
"Quality of Life" should be the label on the right
"Years Since Diagnosis" should be the label on the bottom
Nice to have
• A color scheme that goes from GOOD (low numbers) to BAD (high numbers).

Easy to read (elderly)

```html
<!DOCTYPE html>
<html lang="en">
<head>
<meta charset="utf-8">
<title>Patient-Perceived Progression of Parkinsonism</title>
<link rel="stylesheet" href="https://fonts.googleapis.com/css2?family=Merriweather:wght@700;900&family=Source+Sans+3:ital,wght@0,400;0,600;1,400;1,600;1,700&display=swap">
<style>
  :root {
    --backdrop: #d4d4d4;
    --card: #f8f8f8;
    --panel: #e8e8ea;
    --ink: #111111;
    --accent-red: #c0161f;
    --poor: #b81c2a;
    --fair: #ee7b5a;
    --good: #c9dc82;
    --very-good: #89c14d;
    --excellent: #6a9e3c;
    --grid: #ffffff;
  }
  * { box-sizing: border-box; margin: 0; padding: 0; }
  html, body {
    width: 1070px; height: 1200px; overflow: hidden;
    background: var(--backdrop);
  }
  .poster {
    position: absolute; left: 81px; top: 1px;
    width: 908px; height: 1198px;
    background: var(--card);
    font-family: "Source Sans 3", sans-serif;
    color: var(--ink);
  }
  .poster__title {
    position: absolute; left: 43px; top: 40px;
    font-family: "Merriweather", serif; font-weight: 900;
    font-size: 36px; line-height: 44px; letter-spacing: 0.2px;
  }
  .poster__year {
    position: absolute; left: 776px; top: 44px;
    border-left: 4px solid var(--ink);
    padding-left: 15px;
    font-family: "Merriweather", serif; font-weight: 900;
    font-size: 28px; line-height: 36px; color: var(--accent-red);
  }
  .poster__author {
    position: absolute; right: 41px; top: 101px;
    font-style: italic; font-weight: 600; font-size: 19px;
  }
  .study-link { position: absolute; top: 154px; }
  .study-link--details { left: 43px; }
  .study-link--join { right: 41px; text-align: right; }
  .study-link__label {
    display: block; color: var(--accent-red);
    font-style: italic; font-size: 19px; line-height: 24px;
  }
  .study-link__url {
    display: block; font-family: "Merriweather", serif; font-weight: 700;
    font-size: 17px; line-height: 26px;
  }
  .panel {
    position: absolute; left: 23px; width: 860px;
    background: var(--panel);
  }
  .panel--progression { top: 230px; height: 520px; }
  .panel--survey { top: 771px; height: 397px; }
  .panel svg { display: block; width: 100%; height: 100%; }
  .axis-title { font-family: "Source Sans 3", sans-serif; font-style: italic; font-weight: 700; fill: var(--ink); }
  .tick-label { font-family: "Source Sans 3", sans-serif; font-size: 16px; fill: var(--ink); }
  .band-label { font-family: "Source Sans 3", sans-serif; font-size: 15px; fill: var(--ink); }
  .chart-heading { font-family: "Merriweather", serif; font-weight: 700; font-size: 19px; fill: var(--ink); }
</style>
</head>
<body>
<main class="poster">
  <h1 class="poster__title">Patient - Perceived<br>Progression of Parkinsonism</h1>
  <div class="poster__year">2020</div>
  <p class="poster__author">RT Vandermeer et al.</p>

  <p class="study-link study-link--details">
    <span class="study-link__label">For study details:</span>
    <span class="study-link__url">www.LivingWellWithMovement.org</span>
  </p>
  <p class="study-link study-link--join">
    <span class="study-link__label">To participate in this study:</span>
    <span class="study-link__url">www.WellbeingStudy.Northfield.edu</span>
  </p>

  <section class="panel panel--progression" aria-label="SAW-MX score by years since diagnosis">
    <svg viewBox="0 0 782 473" xmlns="http://www.w3.org/2000/svg">
      <!-- quality bands -->
      <rect x="157" y="36" width="556" height="22" fill="var(--poor)"/>
      <rect x="157" y="58" width="556" height="101" fill="var(--fair)"/>
      <rect x="157" y="159" width="556" height="63" fill="var(--good)"/>
      <rect x="157" y="222" width="556" height="42" fill="var(--very-good)"/>
      <rect x="157" y="264" width="556" height="121" fill="var(--excellent)"/>

      <text class="band-label" x="700" y="53" text-anchor="end" fill="#ffffff" style="fill:#fff;font-size:14px">Poor</text>
      <text class="band-label" x="700" y="112" text-anchor="end">Fair</text>
      <text class="band-label" x="700" y="193" text-anchor="end">Good</text>
      <text class="band-label" x="700" y="252" text-anchor="end">Very Good</text>
      <text class="band-label" x="700" y="330" text-anchor="end">Excellent</text>

      <!-- confidence band and mean curve -->
      <path d="M175,253 C210,245 250,228 300,205 S370,190 420,190 S500,160 560,128 S640,95 660,70 L660,143 C630,130 600,132 560,145 C520,160 470,195 420,206 C380,212 340,205 300,220 C250,240 200,285 175,308 Z" fill="#ffffff" fill-opacity="0.32"/>
      <line x1="175" y1="253" x2="175" y2="308" stroke="#ffffff" stroke-opacity="0.6"/>
      <line x1="660" y1="70" x2="660" y2="143" stroke="#ffffff" stroke-opacity="0.5"/>
      <path d="M175,253 C210,245 250,228 300,205 S370,190 420,190 S500,160 560,128 S640,95 660,70" fill="none" stroke="#111" stroke-width="1.2" stroke-dasharray="4 3"/>
      <path d="M175,308 C200,285 250,240 300,220 S370,205 420,206 S500,175 560,145 S630,130 660,143" fill="none" stroke="#111" stroke-width="1.2" stroke-dasharray="4 3"/>
      <path d="M175,280 C215,262 250,232 300,212 S370,196 420,198 S490,178 540,150 S620,118 660,106" fill="none" stroke="#111" stroke-width="1.6"/>

      <!-- y axis -->
      <g stroke-width="4">
        <line x1="150" y1="132" x2="157" y2="132" stroke="var(--fair)"/>
        <line x1="150" y1="184" x2="157" y2="184" stroke="var(--good)"/>
        <line x1="150" y1="237" x2="157" y2="237" stroke="var(--very-good)"/>
        <line x1="150" y1="291" x2="157" y2="291" stroke="var(--excellent)"/>
        <line x1="150" y1="344" x2="157" y2="344" stroke="var(--excellent)"/>
      </g>
      <g text-anchor="end">
        <text class="tick-label" x="144" y="138">1000</text>
        <text class="tick-label" x="144" y="190">800</text>
        <text class="tick-label" x="144" y="243">600</text>
        <text class="tick-label" x="144" y="297">400</text>
        <text class="tick-label" x="144" y="350">200</text>
      </g>
      <text class="axis-title" font-size="20" text-anchor="middle" transform="translate(50 225) rotate(-90)">
        <tspan x="0" y="0">SAW-MX (Self-Assessed Wellbeing</tspan>
        <tspan x="0" y="29">Index for Movement Conditions)</tspan>
      </text>
      <text class="axis-title" font-size="20" text-anchor="middle" transform="translate(752 200) rotate(-90)">Quality Of Life</text>

      <!-- x axis -->
      <g stroke="var(--excellent)" stroke-width="4">
        <line x1="175" y1="385" x2="175" y2="394"/>
        <line x1="336" y1="385" x2="336" y2="394"/>
        <line x1="498" y1="385" x2="498" y2="394"/>
        <line x1="660" y1="385" x2="660" y2="394"/>
      </g>
      <g text-anchor="middle">
        <text class="tick-label" x="175" y="414">0</text>
        <text class="tick-label" x="336" y="414">5</text>
        <text class="tick-label" x="498" y="414">10</text>
        <text class="tick-label" x="660" y="414">15</text>
      </g>
      <text class="axis-title" font-size="18" x="437" y="444" text-anchor="middle">Years Since Diagnosis</text>
      <g stroke="#111" stroke-width="1.2" fill="#111">
        <line x1="164" y1="439" x2="334" y2="439"/>
        <path d="M159,439 l8,-3.5 v7 z"/>
        <line x1="538" y1="439" x2="708" y2="439"/>
        <path d="M713,439 l-8,-3.5 v7 z"/>
      </g>
    </svg>
  </section>

  <section class="panel panel--survey" aria-label="SAW-MX score by self-rated quality of life">
    <svg viewBox="0 0 782 361" xmlns="http://www.w3.org/2000/svg">
      <text class="chart-heading" x="383" y="48" text-anchor="middle">In General, Would You Say Your Quality of Life is:</text>

      <g stroke="var(--grid)" stroke-width="1.2">
        <line x1="124" y1="89" x2="737" y2="89"/>
        <line x1="124" y1="143" x2="737" y2="143"/>
        <line x1="124" y1="198" x2="737" y2="198"/>
        <line x1="124" y1="252" x2="737" y2="252"/>
        <line x1="124" y1="307" x2="737" y2="307"/>
      </g>
      <g text-anchor="end">
        <text class="tick-label" x="105" y="94" style="font-size:15px">2000</text>
        <text class="tick-label" x="105" y="148" style="font-size:15px">1500</text>
        <text class="tick-label" x="105" y="203" style="font-size:15px">1000</text>
        <text class="tick-label" x="105" y="257" style="font-size:15px">500</text>
        <text class="tick-label" x="105" y="312" style="font-size:15px">0</text>
      </g>
      <text class="axis-title" font-size="18" text-anchor="middle" transform="translate(42 198) rotate(-90)">SAW-MX</text>

      <rect x="127" y="252.3" width="59" height="54.7" fill="var(--excellent)"/>
      <rect x="246" y="235" width="59" height="72" fill="var(--very-good)"/>
      <rect x="365" y="209.4" width="59" height="97.6" fill="var(--good)"/>
      <rect x="484" y="168.8" width="59" height="138.2" fill="var(--fair)"/>
      <rect x="603" y="126.6" width="59" height="180.4" fill="var(--poor)"/>

      <g text-anchor="middle" style="font-size:14px">
        <text class="tick-label" x="156.5" y="246" style="font-size:14px">502</text>
        <text class="tick-label" x="275.5" y="229" style="font-size:14px">661</text>
        <text class="tick-label" x="394.5" y="203" style="font-size:14px">895</text>
        <text class="tick-label" x="513.5" y="163" style="font-size:14px">1268</text>
        <text class="tick-label" x="632.5" y="121" style="font-size:14px">1655</text>
      </g>
      <g text-anchor="middle">
        <text class="tick-label" x="157" y="335">Excellent</text>
        <text class="tick-label" x="272" y="335">Very Good</text>
        <text class="tick-label" x="396" y="335">Good</text>
        <text class="tick-label" x="515" y="335">Fair</text>
        <text class="tick-label" x="635" y="335">Poor</text>
      </g>
    </svg>
  </section>
</main>
</body>
</html>
```